Need Power Point Presentation - That incorporates New Logo

We have a new logo and would like to incorporate it into a Power Point template. We are looking for title page, 2 body pages and a closing page design. If you have any questions please let me know. New logo is attached.

```html
<!DOCTYPE html>
<html lang="en">
<head>
<meta charset="utf-8">
<title>Norval – Presentation Template</title>
<link href="https://fonts.googleapis.com/css2?family=Arimo:wght@400;700&display=swap" rel="stylesheet">
<style>
:root{
  --page:#e6e6e6;
  --white:#ffffff;
  --sky:#4aaee6;
  --corner:#46b6ea;
  --cyan:#7ff1f7;
  --band-a:#1a9fe8;
  --band-b:#22c3f1;
  --navy:#1f5fa8;
  --title-blue:#1f72c4;
  --link-blue:#3aa0e0;
  --muted:#7fd0f5;
  --ink:#555555;
  --body:#888888;
  --placeholder:#d6d6d6;
  --rule:#dddddd;
  --donut-1:#0a5a9c;
  --donut-2:#4cc3ef;
  --donut-3:#94d3ec;
  --donut-4:#5ab3e6;
  --legend-3:#8dc63f;
  --legend-4:#8a6fb0;
  --social:#cfcfcf;
}
*{margin:0;padding:0;box-sizing:border-box}
html,body{width:787px;height:1200px;overflow:hidden;background:var(--page)}
body{position:relative;font-family:"Arimo",Arial,sans-serif}
.defs{position:absolute;width:0;height:0}
.slide{position:absolute;width:357px;height:267px;overflow:hidden;background:var(--white)}
.slide > .bg{position:absolute;left:0;top:0;width:357px;height:267px}
.abs{position:absolute}
.brand{position:absolute;display:flex;align-items:center;gap:3px;color:var(--white);font-weight:700;font-size:11px;letter-spacing:.5px}
.brand-dot{width:7px;height:7px;border-radius:50%;background:currentColor}
.brand--hero{color:var(--sky);font-size:38px;gap:8px;letter-spacing:2px}
.brand--hero .brand-dot{width:20px;height:20px}
.footer-num{position:absolute;top:246px;left:27px;font-size:7px;color:var(--white);font-weight:700}
.footer-title{position:absolute;top:246px;left:73px;font-size:7px;color:var(--muted)}
.footer-sub{position:absolute;top:246px;left:178px;font-size:7px;color:var(--white);font-weight:700}
.slide .brand.footer-brand{top:244px;left:283px}
.kicker{font-size:10px;color:var(--link-blue)}
.headline{font-size:22px;font-weight:700;color:var(--title-blue);line-height:1}
.subhead{font-size:12px;font-weight:700;color:var(--title-blue)}
.agenda-title{font-size:12px;font-weight:700;color:var(--ink)}
.topic{font-size:8px;font-weight:700;color:var(--title-blue)}
.agenda-item{display:flex;align-items:center;width:256px;font-size:8px;color:var(--body)}
.agenda-item .tri{width:0;height:0;border-top:3.5px solid transparent;border-bottom:3.5px solid transparent;border-left:5px solid var(--link-blue);margin-right:10px;margin-left:2px}
.agenda-item .leader{flex:1;border-bottom:1px dotted #aaa;margin:0 6px 0 3px;transform:translateY(2px)}
.agenda-item .num{font-size:7px;color:var(--title-blue)}
.label{font-size:8px;font-weight:700;color:var(--navy)}
.job{font-size:7px;color:var(--link-blue)}
.copy{font-size:5px;line-height:1.35;color:var(--body)}
.bullet{display:flex;gap:11px;width:135px}
.bullet .arrow{flex:none;width:0;height:0;border-top:8px solid transparent;border-bottom:8px solid transparent;border-left:9px solid var(--link-blue)}
.photo{position:absolute;background:var(--placeholder);display:flex;align-items:center;justify-content:center}
.photo--round{border-radius:50%}
.thanks{font-size:36px;font-weight:700;color:var(--sky)}
.social{position:absolute;top:126px;width:18px;height:18px;border-radius:50%;background:var(--social)}
.contact{font-size:6px;color:var(--white);line-height:1.35}
.legend-key{width:5px;height:5px}
.legend-name{font-size:7px;color:var(--link-blue)}
</style>
</head>
<body>

<svg class="defs" aria-hidden="true">
  <defs>
    <linearGradient id="band-fill" x1="0" y1="0" x2="1" y2="0">
      <stop offset="0" stop-color="#1a9fe8"/>
      <stop offset="1" stop-color="#22c3f1"/>
    </linearGradient>
    <linearGradient id="hero-fill" x1="0" y1="0" x2="1" y2="1">
      <stop offset="0" stop-color="#1e9fe8"/>
      <stop offset=".5" stop-color="#168ee0"/>
      <stop offset="1" stop-color="#1fb6ee"/>
    </linearGradient>
    <linearGradient id="cyan-fill" x1="0" y1="0" x2="1" y2="1">
      <stop offset="0" stop-color="#8ef6f9"/>
      <stop offset="1" stop-color="#5fe4f4"/>
    </linearGradient>
    <linearGradient id="panel-fill" x1="0" y1="0" x2="0" y2="1">
      <stop offset="0" stop-color="#3fe0f7"/>
      <stop offset="1" stop-color="#b4fafc"/>
    </linearGradient>
    <symbol id="hero-bg" viewBox="0 0 357 267">
      <rect width="357" height="267" fill="#fff"/>
      <polygon points="310,0 357,0 357,60" fill="#4ab0e6"/>
      <polygon points="0,100 0,163 80,163" fill="url(#cyan-fill)"/>
      <rect y="163" width="357" height="104" fill="url(#hero-fill)"/>
      <polygon points="85,163 150,163 240,267 175,267" fill="#0d5fb8" opacity=".4"/>
      <polygon points="0,190 0,267 60,267" fill="#3fc9f2" opacity=".5"/>
      <polygon points="230,163 357,163 357,267 320,267" fill="#35c6f2" opacity=".45"/>
    </symbol>
    <symbol id="body-bg" viewBox="0 0 357 267">
      <rect width="357" height="267" fill="#fff"/>
      <polygon points="305,0 357,0 357,55" fill="#46b6ea"/>
      <polygon points="0,160 0,234 62,234" fill="url(#cyan-fill)"/>
      <rect y="234" width="357" height="33" fill="url(#band-fill)"/>
      <polygon points="50,234 95,234 125,267 80,267" fill="#0f63bd" opacity=".5"/>
      <polygon points="150,234 357,234 357,267 175,267" fill="#2cc7f2" opacity=".6"/>
    </symbol>
    <symbol id="image-icon" viewBox="0 0 30 26">
      <rect x="1" y="1" width="28" height="24" fill="none" stroke="#fff" stroke-width="2"/>
      <circle cx="20" cy="8" r="2.5" fill="#fff"/>
      <polygon points="4,21 12,11 18,18 21,15 26,21" fill="#fff"/>
    </symbol>
  </defs>
</svg>

<!-- Cover -->
<section class="slide" style="left:30px;top:28px">
  <svg class="bg"><use href="#hero-bg"/></svg>
  <div class="brand brand--hero" style="left:60px;top:95px"><span class="brand-dot"></span>NORVAL</div>
</section>

<!-- Title -->
<section class="slide" style="left:398px;top:28px">
  <svg class="bg"><use href="#hero-bg"/></svg>
  <div class="abs kicker" style="left:57px;top:53px">COMPANY PRESENTATION</div>
  <div class="abs headline" style="left:57px;top:67px">TITLE HERE</div>
  <div class="abs subhead" style="left:57px;top:89px">Presentation Subtitle</div>
  <div class="brand" style="left:285px;top:241px"><span class="brand-dot"></span>NORVAL</div>
</section>

<!-- Agenda -->
<section class="slide" style="left:30px;top:302px">
  <svg class="bg"><use href="#body-bg"/></svg>
  <svg class="abs" style="left:0;top:0" width="357" height="234" aria-hidden="true">
    <rect x="308" width="49" height="234" fill="url(#panel-fill)"/>
    <polygon points="308,0 357,0 357,55" fill="#6fd8f4"/>
    <polygon points="0,170 0,234 62,234" fill="url(#cyan-fill)"/>
  </svg>
  <div class="abs agenda-title" style="left:37px;top:34px">TODAY'S AGENDA</div>
  <div class="abs topic" style="left:38px;top:53px">TOPIC TITLE</div>
  <div class="abs agenda-item" style="left:38px;top:64px"><span class="tri"></span>Topic Subtitle<span class="leader"></span><span class="num">#</span></div>
  <div class="abs agenda-item" style="left:38px;top:75px"><span class="tri"></span>Topic Subtitle<span class="leader"></span><span class="num">#</span></div>
  <div class="abs agenda-item" style="left:38px;top:86px"><span class="tri"></span>Topic Subtitle<span class="leader"></span><span class="num">#</span></div>
  <div class="abs topic" style="left:38px;top:114px">TOPIC TITLE</div>
  <div class="abs agenda-item" style="left:38px;top:127px"><span class="tri"></span>Topic Subtitle<span class="leader"></span><span class="num">#</span></div>
  <div class="abs agenda-item" style="left:38px;top:138px"><span class="tri"></span>Topic Subtitle<span class="leader"></span><span class="num">#</span></div>
  <div class="abs topic" style="left:38px;top:165px">TOPIC TITLE</div>
  <div class="abs agenda-item" style="left:38px;top:178px"><span class="tri"></span>Topic Subtitle<span class="leader"></span><span class="num">#</span></div>
  <div class="abs agenda-item" style="left:38px;top:189px"><span class="tri"></span>Topic Subtitle<span class="leader"></span><span class="num">#</span></div>
  <div class="abs agenda-item" style="left:38px;top:200px"><span class="tri"></span>Topic Subtitle<span class="leader"></span><span class="num">#</span></div>
  <div class="footer-title">PRESENTATION TITLE</div>
  <div class="footer-sub">Presentation Subtitle</div>
  <div class="brand footer-brand"><span class="brand-dot"></span>NORVAL</div>
</section>

<!-- Company -->
<section class="slide" style="left:398px;top:302px">
  <svg class="bg"><use href="#body-bg"/></svg>
  <div class="abs label" style="left:27px;top:24px">COMPANY NAME</div>
  <p class="abs copy" style="left:27px;top:52px;width:130px">Lorem ipsum dolor sit amet, consectetur adipiscing elit. Aliquam eget bibendum dui. Nunc tristique, orci non dictum sollicitudin, metus mauris malesuada diam, quis mollis odio libero in ante.</p>
  <div class="abs bullet" style="left:27px;top:92px"><span class="arrow"></span><p class="copy">Lorem ipsum dolor sit amet, consectetur adipiscing elit. Aliquam eget bibendum dui libero in ante lacus.</p></div>
  <div class="abs bullet" style="left:27px;top:121px"><span class="arrow"></span><p class="copy">Lorem ipsum dolor sit amet, consectetur adipiscing elit. Aliquam eget bibendum dui libero in ante lacus.</p></div>
  <div class="abs bullet" style="left:27px;top:150px"><span class="arrow"></span><p class="copy">Lorem ipsum dolor sit amet, consectetur adipiscing elit. Aliquam eget bibendum dui libero in ante lacus.</p></div>
  <div class="abs bullet" style="left:27px;top:179px"><span class="arrow"></span><p class="copy">Lorem ipsum dolor sit amet, consectetur adipiscing elit. Aliquam eget bibendum dui libero in ante lacus.</p></div>
  <div class="photo" role="img" aria-label="Company photo" style="left:196px;top:22px;width:136px;height:190px"><svg width="54" height="46"><use href="#image-icon"/></svg></div>
  <div class="footer-num">1</div>
  <div class="footer-title">PRESENTATION TITLE</div>
  <div class="footer-sub">Presentation Subtitle</div>
  <div class="brand footer-brand"><span class="brand-dot"></span>NORVAL</div>
</section>

<!-- Team -->
<section class="slide" style="left:30px;top:576px">
  <svg class="bg"><use href="#body-bg"/></svg>
  <div class="photo photo--round" role="img" aria-label="Team member portrait" style="left:23px;top:13px;width:85px;height:85px"><svg width="26" height="23"><use href="#image-icon"/></svg></div>
  <div class="photo photo--round" role="img" aria-label="Team member portrait" style="left:136px;top:13px;width:85px;height:85px"><svg width="26" height="23"><use href="#image-icon"/></svg></div>
  <div class="photo photo--round" role="img" aria-label="Team member portrait" style="left:248px;top:13px;width:85px;height:85px"><svg width="26" height="23"><use href="#image-icon"/></svg></div>
  <div class="abs" style="left:30px;top:139px;width:80px;text-align:center"><div class="label">NAME HERE</div><div class="job">Job title</div></div>
  <div class="abs" style="left:143px;top:139px;width:80px;text-align:center"><div class="label">NAME HERE</div><div class="job">Job title</div></div>
  <div class="abs" style="left:255px;top:139px;width:80px;text-align:center"><div class="label">NAME HERE</div><div class="job">Job title</div></div>
  <p class="abs copy" style="left:31px;top:164px;width:72px">Lorem ipsum dolor sit amet, consectetur adipiscing elit. Aliquam eget bibendum dui libero in ante lacus.</p>
  <p class="abs copy" style="left:144px;top:164px;width:72px">Lorem ipsum dolor sit amet, consectetur adipiscing elit. Aliquam eget bibendum dui libero in ante lacus.</p>
  <p class="abs copy" style="left:257px;top:164px;width:72px">Lorem ipsum dolor sit amet, consectetur adipiscing elit. Aliquam eget bibendum dui libero in ante lacus.</p>
  <div class="footer-num">2</div>
  <div class="footer-title">PRESENTATION TITLE</div>
  <div class="footer-sub">Presentation Subtitle</div>
  <div class="brand footer-brand"><span class="brand-dot"></span>NORVAL</div>
</section>

<!-- Profiles -->
<section class="slide" style="left:398px;top:576px">
  <svg class="bg"><use href="#body-bg"/></svg>
  <div class="photo" role="img" aria-label="Featured profile photo" style="left:25px;top:29px;width:138px;height:81px"><svg width="26" height="23"><use href="#image-icon"/></svg></div>
  <div class="abs label" style="left:197px;top:28px">NAME HERE</div>
  <p class="abs copy" style="left:197px;top:41px;width:135px">Lorem ipsum dolor sit amet, consectetur adipiscing elit. Aliquam eget bibendum dui. Nunc tristique, orci non dictum sollicitudin, metus mauris malesuada diam, quis mollis odio libero in ante. Cras sodales enim in purus venenatis volutpat. Aliquam quis enim nec risus pellentesque viverra. Nam sit amet est accumsan, mattis enim ut, venenatis mauris.</p>
  <div class="abs" style="left:25px;top:121px;width:302px;height:1px;background:var(--rule)"></div>
  <div class="photo" role="img" aria-label="Profile photo" style="left:25px;top:152px;width:50px;height:35px"><svg width="18" height="16"><use href="#image-icon"/></svg></div>
  <div class="abs" style="left:88px;top:150px"><div class="label">NAME HERE</div><div class="job">Job title</div></div>
  <p class="abs copy" style="left:89px;top:168px;width:72px">Lorem ipsum dolor sit amet, consectetur adipiscing elit. Aliquam eget bibendum dui.</p>
  <div class="photo" role="img" aria-label="Profile photo" style="left:198px;top:152px;width:50px;height:35px"><svg width="18" height="16"><use href="#image-icon"/></svg></div>
  <div class="abs" style="left:261px;top:150px"><div class="label">NAME HERE</div><div class="job">Job title</div></div>
  <p class="abs copy" style="left:262px;top:168px;width:72px">Lorem ipsum dolor sit amet, consectetur adipiscing elit. Aliquam eget bibendum dui.</p>
  <div class="footer-num">3</div>
  <div class="footer-title">PRESENTATION TITLE</div>
  <div class="footer-sub">Presentation Subtitle</div>
  <div class="brand footer-brand"><span class="brand-dot"></span>NORVAL</div>
</section>

<!-- Chart -->
<section class="slide" style="left:30px;top:853px">
  <svg class="bg"><use href="#body-bg"/></svg>
  <svg class="abs" style="left:27px;top:37px" width="140" height="140" viewBox="0 0 140 140" role="img" aria-label="Donut chart of four series">
    <g transform="rotate(-90 70 70)" fill="none" stroke-width="37">
      <circle cx="70" cy="70" r="51.5" stroke="var(--donut-1)" stroke-dasharray="193.2 323.6"/>
      <circle cx="70" cy="70" r="51.5" stroke="var(--donut-2)" stroke-dasharray="67.4 323.6" stroke-dashoffset="-193.2"/>
      <circle cx="70" cy="70" r="51.5" stroke="var(--donut-3)" stroke-dasharray="36 323.6" stroke-dashoffset="-260.6"/>
      <circle cx="70" cy="70" r="51.5" stroke="var(--donut-4)" stroke-dasharray="27 323.6" stroke-dashoffset="-296.6"/>
    </g>
    <circle cx="70" cy="70" r="69.5" fill="none" stroke="#c9d6e0" stroke-width=".6"/>
  </svg>
  <div class="abs" style="left:192px;top:33px;width:140px">
    <div style="display:flex;align-items:center;gap:8px"><span class="legend-key" style="background:var(--donut-1)"></span><span class="legend-name">Serie 1</span></div>
    <p class="copy" style="margin:3px 0 0 13px">Lorem ipsum dolor sit amet, consectetur adipiscing elit. Aliquam eget bibendum dui.</p>
  </div>
  <div class="abs" style="left:192px;top:75px;width:140px">
    <div style="display:flex;align-items:center;gap:8px"><span class="legend-key" style="background:var(--donut-2)"></span><span class="legend-name">Serie 1</span></div>
    <p class="copy" style="margin:3px 0 0 13px">Lorem ipsum dolor sit amet, consectetur adipiscing elit. Aliquam eget bibendum dui.</p>
  </div>
  <div class="abs" style="left:192px;top:116px;width:140px">
    <div style="display:flex;align-items:center;gap:8px"><span class="legend-key" style="background:var(--legend-3)"></span><span class="legend-name">Serie 1</span></div>
    <p class="copy" style="margin:3px 0 0 13px">Lorem ipsum dolor sit amet, consectetur adipiscing elit. Aliquam eget bibendum dui.</p>
  </div>
  <div class="abs" style="left:192px;top:157px;width:140px">
    <div style="display:flex;align-items:center;gap:8px"><span class="legend-key" style="background:var(--legend-4)"></span><span class="legend-name">Serie 1</span></div>
    <p class="copy" style="margin:3px 0 0 13px">Lorem ipsum dolor sit amet, consectetur adipiscing elit. Aliquam eget bibendum dui.</p>
  </div>
  <div class="footer-num">4</div>
  <div class="footer-title">PRESENTATION TITLE</div>
  <div class="footer-sub">Presentation Subtitle</div>
  <div class="brand footer-brand"><span class="brand-dot"></span>NORVAL</div>
</section>

<!-- Closing -->
<section class="slide" style="left:398px;top:853px">
  <svg class="bg"><use href="#hero-bg"/></svg>
  <div class="abs thanks" style="left:0;top:68px;width:357px;text-align:center">Thanks</div>
  <span class="social" style="left:122px"></span>
  <span class="social" style="left:146px"></span>
  <span class="social" style="left:169px"></span>
  <span class="social" style="left:192px"></span>
  <span class="social" style="left:216px"></span>
  <div class="abs contact" style="left:8px;top:212px;font-weight:700">http://www.norval.com/</div>
  <div class="abs contact" style="left:8px;top:226px">info@norval.com</div>
  <div class="abs contact" style="left:8px;top:238px">48 Harbor Lane, Suite 12<br>Marlow, Ohio<br>40112 USA</div>
  <div class="brand" style="left:285px;top:247px"><span class="brand-dot"></span>NORVAL</div>
</section>

</body>
</html>
```